Business Card Design Project

I need a business card designed from scratch. I have an existing logo that I can upload in Illustrator for modification or redesign.

The Company is called Ranking Oracles http://rankingoracles.com.au and we provide Search Engine Optimization services to Australian businesses. The current logo signifies an increase in visitors, profits etc...

There are no restrictions as to the redesign - colours, style etc are all open to change.

Cards will be full colour and one sided printed at http://www.cardmillo.com.au so check their requirements for file format and sizes etc.

I will expect all original files upon completion of project.

Target Market(s)

Any business with a web site looking to improve their search engine rankings

Industry/Entity Type

Business

Requirements
Must have
• I like modern, sleek designs. Clean, not fussy, uncluttered.

```html
<!DOCTYPE html>
<html lang="en">
<head>
<meta charset="utf-8">
<title>Ranking Oracles – Business Card</title>
<link href="https://fonts.googleapis.com/css2?family=Arimo:wght@400;700&display=swap" rel="stylesheet">
<style>
  :root {
    --backdrop: #9a9a9a;
    --card: #f4f4f2;
    --brand-blue: #1a75a8;
    --logo-blue: #1b5fae;
    --accent-yellow: #f6b81c;
    --ink: #111111;
    --white: #ffffff;
  }
  * { box-sizing: border-box; margin: 0; padding: 0; }
  html, body {
    width: 1200px; height: 720px; overflow: hidden;
    background: var(--backdrop);
    font-family: "Arimo", Arial, sans-serif;
  }
  .stage {
    width: 1200px; height: 720px;
    display: flex; align-items: center; justify-content: center;
  }
  .business-card {
    position: relative;
    width: 980px; height: 560px;
    background: var(--card);
    overflow: hidden;
    box-shadow: 0 6px 20px rgba(0,0,0,0.25);
  }
  .brand {
    position: absolute; left: 60px; top: 48px;
    display: flex; align-items: center; gap: 18px;
  }
  .brand-mark {
    width: 46px; height: 46px; border-radius: 50%;
    background: var(--accent-yellow);
  }
  .brand-text { color: var(--logo-blue); font-weight: 700; }
  .brand-name { font-size: 44px; line-height: 1; letter-spacing: -0.5px; }
  .brand-tagline { font-size: 20px; margin-top: 4px; }
  .name-band {
    position: absolute; left: 0; top: 180px;
    width: 660px; height: 78px;
    background: var(--brand-blue);
    clip-path: polygon(0 0, 100% 0, 94% 100%, 0 100%);
    display: flex; align-items: center;
    padding-left: 60px;
  }
  .person-name {
    color: var(--white); font-size: 40px; font-weight: 400;
  }
  .accent-band {
    position: absolute; right: 0; top: 240px;
    width: 320px; height: 66px;
    background: var(--accent-yellow);
    clip-path: polygon(10% 0, 100% 0, 100% 100%, 0 100%);
  }
  .contact-details {
    position: absolute; left: 330px; top: 336px;
    list-style: none;
    color: var(--ink); font-size: 27px; line-height: 1.22;
  }
</style>
</head>
<body>
<main class="stage">
  <article class="business-card">
    <header class="brand">
      <span class="brand-mark" aria-hidden="true"></span>
      <div class="brand-text">
        <div class="brand-name">Ranking Oracles</div>
        <div class="brand-tagline">Oracles For Rankings</div>
      </div>
    </header>

    <div class="name-band">
      <h1 class="person-name">Daniel Whitmore</h1>
    </div>

    <div class="accent-band" aria-hidden="true"></div>

    <ul class="contact-details">
      <li>14 Harbour Lane, Ultimo, Sydney, Australia</li>
      <li>Cell: 0412-738290</li>
      <li>Tel: 9281 4470</li>
      <li>E: hello@rankingoracles.com.au</li>
      <li>W: www.RankingOracles.com.au</li>
    </ul>
  </article>
</main>
</body>
</html>
```